Assessment Report cover design and formatting

This report is for senior executives and provides leaders with detailed insight into their capabilities and skills. The cover should have space for the date and name of the person doing the assessment. We are looking to modernise the report cover design. We would like the report to be our company colours if possible. The work will likely expand once the cover is done to other parts of the report, ie. the format and layout of the report etc.

Company colours:
Primary colours:
• Blue #0D47A1, #115CD0, #90B6ED, #EEf3FB
• Green #0D91A1, #47A10D, #324C196, #0DA11D
Additional colours:
• Purple #A10D91
• Brown #A1670D
• Red #A10D47

Target Market(s)

Executives

Industry/Entity Type

Consulting, leadership development

Colors
0094D4
00A9DD
6FCCEA
C7EBF8
E9F6FB
00AB8E
00BBA5
67D7C9
C6EFE9
E9F9F6
E54698
E96AAD
F1A4CE
F9D9EA
FCEFF6
6B429C
8869AF
B7A5CE
E3DAEB
F3F0F8

Requirements
Must have
• The report cover should have space for name of user, the date and company logo. Cover should be in A4 size.

```html
<!DOCTYPE html>
<html lang="en">
<head>
<meta charset="UTF-8">
<title>Leadership Assessment Report – Cover</title>
<link href="https://fonts.googleapis.com/css2?family=Montserrat:wght@300;400;600;700;800&display=swap" rel="stylesheet">
<style>
  :root {
    --stage: #c4c4c4;
    --cover-blue: #3352a8;
    --cover-blue-deep: #1e2f7e;
    --contour-teal: #2fa7b8;
    --accent-teal: #3fe0cf;
    --band-teal: #2cc9b5;
    --paper: #efefef;
    --logo-blue: #2a45b8;
    --white: #ffffff;
  }
  * { box-sizing: border-box; margin: 0; padding: 0; }
  html, body {
    width: 1200px;
    height: 800px;
    overflow: hidden;
    background: var(--stage);
    font-family: "Montserrat", sans-serif;
  }
  .canvas {
    width: 1200px;
    height: 800px;
    display: flex;
    align-items: center;
    justify-content: center;
  }
  .report-cover {
    position: relative;
    width: 524px;
    height: 741px;
    background: var(--paper);
    overflow: hidden;
    box-shadow: 0 10px 30px rgba(0,0,0,0.18);
  }
  .cover-artwork {
    position: absolute;
    inset: 0;
    background:
      radial-gradient(ellipse at 30% 25%, rgba(70,110,200,0.35), transparent 60%),
      linear-gradient(160deg, var(--cover-blue) 0%, #2c48a0 55%, var(--cover-blue-deep) 100%);
  }
  .cover-footer {
    position: absolute;
    inset: 0;
    width: 100%;
    height: 100%;
  }
  .cover-title {
    position: absolute;
    left: 92px;
    top: 250px;
    width: 360px;
  }
  .title-main {
    display: block;
    color: var(--white);
    font-weight: 700;
    font-size: 47px;
    letter-spacing: 3px;
    line-height: 1;
  }
  .title-sub-row {
    display: flex;
    align-items: flex-start;
    justify-content: space-between;
    margin-top: 4px;
  }
  .title-assessment {
    color: var(--white);
    font-weight: 600;
    font-size: 15px;
    letter-spacing: 1px;
    padding-bottom: 4px;
    border-bottom: 3px solid var(--accent-teal);
  }
  .title-report {
    color: var(--accent-teal);
    font-weight: 700;
    font-size: 38px;
    letter-spacing: 3px;
    line-height: 1;
    margin-top: 2px;
  }
  .cover-details {
    position: absolute;
    left: 92px;
    top: 380px;
    width: 260px;
    color: var(--white);
  }
  .name-field {
    display: flex;
    align-items: baseline;
    gap: 4px;
    font-weight: 600;
    font-size: 14px;
  }
  .name-line {
    flex: 1;
    border-bottom: 1px dotted rgba(255,255,255,0.75);
    height: 1px;
  }
  .report-date {
    margin-top: 10px;
    margin-left: 16px;
    font-weight: 300;
    font-size: 15px;
    letter-spacing: 1px;
  }
  .company-mark {
    position: absolute;
    right: 48px;
    bottom: 52px;
    display: flex;
    align-items: center;
    gap: 10px;
    color: var(--logo-blue);
    font-weight: 600;
    font-size: 20px;
    letter-spacing: 1px;
  }
  .company-dot {
    width: 16px;
    height: 16px;
    border-radius: 50%;
    background: var(--logo-blue);
  }
</style>
</head>
<body>
<main class="canvas">
  <section class="report-cover">
    <div class="cover-artwork" role="img" aria-label="Blue topographic contour-line pattern in teal and light blue lines"></div>

    <svg class="cover-footer" viewBox="0 0 524 741" preserveAspectRatio="none" aria-hidden="true">
      <path d="M0 612 Q 260 640 524 662 L524 741 L0 741 Z" fill="var(--paper)"/>
      <path d="M0 612 Q 260 640 524 662" fill="none" stroke="var(--band-teal)" stroke-width="6"/>
    </svg>

    <h1 class="cover-title">
      <span class="title-main">LEADERSHIP</span>
      <span class="title-sub-row">
        <span class="title-assessment">ASSESSMENT</span>
        <span class="title-report">REPORT</span>
      </span>
    </h1>

    <div class="cover-details">
      <div class="name-field"><span class="name-label">Name:</span><span class="name-line"></span></div>
      <p class="report-date">30 September 2023</p>
    </div>

    <div class="company-mark">
      <span class="company-dot"></span>
      <span class="company-name">Meridian Partners</span>
    </div>
  </section>
</main>
</body>
</html>
```